Web design for business website

I need a web design for a business website for one of our clients who is specialized in alarm management software. I would like you to design 3 web pages, one for each of the 3 pages. You need to process the corporate identity of our client to the web design. This means the colors of the logo (red and black) should definitely show up on all of the 3 pages. Find the logo file for the logo of our customer. To increase readability I suggest you use a white/light background. All suggestions are welcome.

Target Market(s)

B2B, Alarm management

Industry/Entity Type

Business

Number of Pages Required

3 page

Requirements
Must have
• The web design must have exactly the same structure as the wireframes and needs to contain the colors of the company logo.

```html
<!DOCTYPE html>
<html lang="en">
<head>
<meta charset="utf-8">
<title>Verantis – Real-time reasoning solutions</title>
<link rel="stylesheet" href="https://fonts.googleapis.com/css2?family=Raleway:wght@400;500;600;700;800&family=Open+Sans:wght@400;600;700&display=swap">
<style>
:root{
  --accent:#e8470f;
  --ink:#1c1b2e;
  --topbar:#141414;
  --nav:#1d1c33;
  --light:#f5f5f5;
  --text:#666;
  --footer:#141414;
  --footer-text:#5a5a5a;
  --white:#fff;
}
*{margin:0;padding:0;box-sizing:border-box}
html,body{width:689px;height:1200px;overflow:hidden}
body{font-family:'Open Sans',sans-serif;background:var(--white);color:var(--text);font-size:7px;position:relative}
.wrap{position:absolute;left:56px;right:57px}
.abs{position:absolute}
/* top bar */
.topbar{position:absolute;top:0;left:0;width:100%;height:19px;background:var(--topbar);color:#bbb;font-size:7px}
.topbar .phone{left:56px;top:5px;display:flex;gap:5px;align-items:center}
.topbar .tools{right:79px;top:0;display:flex;height:19px;border-left:1px solid #555}
.topbar .tools span{display:flex;align-items:center;gap:5px;padding:0 8px;border-right:1px solid #555;font-size:6.5px}
/* header */
.header{position:absolute;top:19px;left:0;width:100%;height:50px;background:var(--light)}
.logo{left:56px;top:12px;display:flex;align-items:center;gap:6px}
.logo .mark{width:26px;height:26px;border-radius:50%;background:var(--accent)}
.logo .name{font-family:'Raleway',sans-serif;font-weight:800;font-size:20px;color:var(--ink);letter-spacing:1px;line-height:1}
.logo .tag{font-size:5.5px;color:var(--ink);margin-top:1px}
.account{right:79px;top:13px;display:flex;gap:8px}
.account span{width:40px;height:24px;background:#ccc;display:flex;align-items:center;justify-content:center}
.account span:first-child{background:var(--accent)}
/* nav */
.nav{position:absolute;top:69px;left:0;width:100%;height:24px;background:var(--nav)}
.nav ul{list-style:none;display:flex;position:absolute;left:56px;top:0;height:24px}
.nav li{color:#fff;font-size:6.5px;font-weight:600;display:flex;align-items:center;padding:0 14px 0 14px;margin-right:9px}
.nav li.active{background:var(--accent);padding:0 14px}
/* hero */
.hero{position:absolute;top:93px;left:0;width:100%;height:246px;background:linear-gradient(180deg,#2f3840 0%,#5a5a4e 40%,#3d4038 70%,#2a2c2c 100%)}
.hero::after{content:"";position:absolute;inset:0;background:radial-gradient(ellipse at 50% 50%,rgba(0,0,0,.2),rgba(0,0,0,.45))}
.hero .content{position:absolute;left:0;right:0;top:74px;text-align:center;z-index:1;color:#fff}
.welcome{display:flex;align-items:baseline;justify-content:center;gap:5px}
.welcome .w{font-family:'Raleway',sans-serif;font-size:13px}
.welcome .brand{font-family:'Raleway',sans-serif;font-weight:800;font-size:30px;color:var(--accent);letter-spacing:.5px}
.welcome .t{font-size:8.5px}
.hero p{font-size:7px;line-height:1.45;margin:6px auto 0;width:340px}
.btn-light{display:inline-block;margin-top:17px;background:#f0f0f0;color:#333;font-size:6.5px;padding:8px 17px;border:1px solid #ccc}
.arrow{position:absolute;top:100px;width:29px;height:29px;display:flex;align-items:center;justify-content:center;z-index:1}
.arrow.prev{left:28px;background:#fff}
.arrow.next{left:632px;background:var(--accent)}
/* welcome strip */
.intro{position:absolute;top:339px;left:0;width:100%;height:103px;display:flex;align-items:center;justify-content:center;color:var(--ink)}
/* about */
.about{position:absolute;top:442px;left:0;width:100%;height:246px;background:var(--light)}
.about h2{position:absolute;left:57px;top:38px;font-family:'Raleway',sans-serif;font-weight:700;font-size:17px;color:var(--accent)}
.about p{position:absolute;left:57px;top:68px;width:325px;font-size:6.5px;line-height:1.5}
.btn-accent{position:absolute;left:57px;top:174px;background:var(--accent);color:#fff;font-size:6.5px;padding:8px 17px;box-shadow:0 2px 0 #b8360a}
.monitor{position:absolute;left:413px;top:40px;width:219px;height:170px}
.monitor .screen{position:absolute;left:0;top:0;width:219px;height:148px;background:#1a1a1a;border-radius:3px}
.monitor .screen .photo{position:absolute;left:9px;top:10px;width:200px;height:108px;background:linear-gradient(180deg,#e8b36a 0%,#c68345 45%,#7a6550 100%)}
.monitor .chin{position:absolute;left:0;top:125px;width:219px;height:23px;background:#d8d8d8;border-radius:0 0 3px 3px}
.monitor .stand{position:absolute;left:84px;top:148px;width:51px;height:20px;background:linear-gradient(#cfcfcf,#e8e8e8)}
/* clients */
.clients{position:absolute;top:688px;left:0;width:100%;height:100px;text-align:center}
.clients h2{position:absolute;left:220px;width:250px;top:35px;font-family:'Raleway',sans-serif;font-weight:700;font-size:14px;color:var(--accent);border-bottom:1px solid #ccc;padding-bottom:3px}
.clients p{position:absolute;left:0;right:0;top:65px;font-size:8px;color:#777}
.logos{position:absolute;top:788px;left:0;width:100%;height:50px;border-top:1px solid #ddd;border-bottom:1px solid #ddd;display:flex;align-items:center;justify-content:space-around;padding:0 60px}
.logos span{font-family:'Open Sans',sans-serif;font-weight:700;font-size:11px;color:#4a4a4a}
/* social / subscribe */
.connect{position:absolute;top:882px;left:0;width:100%;height:122px;background:linear-gradient(180deg,#1e2226,#2f3235 60%,#24272a)}
.connect h3{position:absolute;top:31px;font-family:'Raleway',sans-serif;font-weight:600;font-size:16px;color:var(--accent)}
.social{position:absolute;left:56px;top:71px;display:flex;gap:5px}
.social span{width:25px;height:25px;background:#9a9a9a}
.social span:first-child{background:#3b5998}
.subscribe{position:absolute;left:253px;top:63px;width:380px;height:25px;border:1px solid #fff;display:flex}
.subscribe .field{flex:1;background:#111;color:#fff;font-size:6.5px;display:flex;align-items:center;padding-left:14px}
.subscribe .go{width:68px;background:#fff;color:var(--accent);font-weight:700;font-size:6.5px;display:flex;align-items:center;justify-content:center}
/* footer */
.footer{position:absolute;top:1004px;left:0;width:100%;height:166px;background:var(--footer)}
.col{position:absolute;top:38px;font-size:6.5px;color:var(--footer-text);line-height:1.65}
.col h4{font-family:'Raleway',sans-serif;font-weight:500;font-size:8.5px;color:#333;margin-bottom:8px}
.col .on{color:var(--accent)}
.col .row{display:flex;gap:8px;align-items:center;margin-bottom:4px}
.bottombar{position:absolute;top:1170px;left:0;width:100%;height:30px;background:var(--footer);border-top:1px solid #222;text-align:center;font-size:5.5px;color:#444;line-height:30px}
.bottombar b{color:var(--accent);font-weight:600}
</style>
</head>
<body>
<div class="topbar">
  <div class="abs phone"><svg width="6" height="6" viewBox="0 0 10 10"><path d="M2 0l2 2-1 2c1 1 2 2 3 3l2-1 2 2-2 2C4 10 0 6 0 2z" fill="#bbb"/></svg>+31 (0)20 5550 148</div>
  <div class="abs tools"><span><svg width="5" height="4"><path d="M0 0h5L2.5 4z" fill="#bbb"/></svg>ENG</span><span><svg width="7" height="7" viewBox="0 0 10 10"><circle cx="4" cy="4" r="3" fill="none" stroke="#bbb" stroke-width="1.5"/><path d="M6 6l3 3" stroke="#bbb" stroke-width="1.5"/></svg></span></div>
</div>

<header class="header">
  <div class="abs logo"><div class="mark"></div><div><div class="name">VERANTIS</div><div class="tag">Real-time reasoning solutions</div></div></div>
  <div class="abs account">
    <span><svg width="7" height="7" viewBox="0 0 10 10"><circle cx="5" cy="3" r="2.5" fill="#fff"/><path d="M0 10c0-4 10-4 10 0z" fill="#fff"/></svg></span>
    <span><svg width="7" height="7" viewBox="0 0 10 10"><rect x="1" y="4" width="6" height="5" fill="#555"/><path d="M5 4V2a2 2 0 014 0v1" fill="none" stroke="#555" stroke-width="1.3"/></svg></span>
    <span><svg width="7" height="7" viewBox="0 0 10 10"><path d="M0 4h5V2l3 3-3 3V6H0z" fill="#555"/><path d="M7 1h2v8H7" fill="none" stroke="#555"/></svg></span>
  </div>
</header>

<nav class="nav"><ul><li class="active">HOME</li><li>INDUSTRY</li><li>TELECOM</li><li>POWER</li><li>UTILITIES</li><li>INFRA</li><li>STORE</li></ul></nav>

<section class="hero" role="img" aria-label="Industrial refinery plant at dusk">
  <div class="arrow prev"><svg width="5" height="7"><path d="M4 0L0 3.5 4 7" fill="none" stroke="#000" stroke-width="1.5"/></svg></div>
  <div class="arrow next"><svg width="5" height="7"><path d="M1 0l4 3.5L1 7" fill="none" stroke="#fff" stroke-width="1.5"/></svg></div>
  <div class="content">
    <div class="welcome"><span class="w">WELCOME TO</span><span class="brand">VERANTIS</span><span class="t">Real-time reasoning solutions</span></div>
    <p>Companies have invested to get data out of processes. New technologies have been developed to get real-time data out of the harshest places, like oil-well drill heads or the Great Barrier Riff.</p>
    <span class="btn-light">LEARN MORE</span>
  </div>
</section>

<section class="intro"><div class="welcome"><span class="w">WELCOME TO</span><span class="brand">VERANTIS</span><span class="t">Real-time reasoning solutions</span></div></section>

<section class="about">
  <h2>ABOUT US</h2>
  <p>Companies have invested to get data out of processes. New technologies have been developed to get real-time data out of the harshest places, like oil-well drill heads or the Great Barrier Riff. Data in itself means nothing without the context the data is collected in. Example: data from equipment under maintenance does not provide information to operations. Information - data which is valid and meaningful can overwhelm any user without the proper knowledge to interpret this information. Verantis technology enables easy application of such knowledge in a comprehensible – visual – representation and makes hypothetical reasoning with information possible providing meaningful advisories to subscribers when they need it or when it is required that they are made aware of a situation which requires their attention.</p>
  <span class="btn-accent">LEARN MORE</span>
  <div class="monitor">
    <div class="screen"><div class="photo" role="img" aria-label="City highway interchange at sunset"></div></div>
    <div class="chin"></div>
    <div class="stand"></div>
  </div>
</section>

<section class="clients">
  <h2>CLIENTS THAT TRUST US</h2>
  <p>Some of our clients that trust us, be shure to be one of them.</p>
</section>
<div class="logos"><span>Corvel</span><span>Norvale</span><span>Bryte</span><span>Delmo</span><span>Hoftmann</span><span>Sheldra</span><span>Marlow Oil</span></div>

<section class="connect">
  <h3 style="left:56px">FOLLOW US ON :</h3>
  <h3 style="left:253px">SUBSCRIBE NOW :</h3>
  <div class="social"><span aria-label="Social network"></span><span aria-label="Social network"></span><span aria-label="Social network"></span><span aria-label="Social network"></span><span aria-label="Video channel"></span></div>
  <div class="subscribe"><div class="field">Enter Your Email Adress</div><div class="go">SUBSCRIBE</div></div>
</section>

<footer class="footer">
  <div class="col" style="left:56px"><h4>SOLUTIONS</h4><div class="on">KAV Alarm Reporting</div><div>KAV Alarm Analysis</div><div>KAV Alarm Expert</div><div>USE</div></div>
  <div class="col" style="left:155px"><h4>INDUSTRIES</h4><div>Industry</div><div>Telecom</div><div>Power</div><div>Utilites</div><div>Infra</div></div>
  <div class="col" style="left:254px"><h4>ABOUT US</h4><div>Company</div><div>Overview</div><div>Leadership</div><div>Partners</div><div>Locations</div></div>
  <div class="col" style="left:352px"><h4>NEWS</h4><div>Product News</div><div>Partner News</div><div>Events</div><div>Press Releases</div><div>Vacancies</div></div>
  <div class="col" style="left:500px"><h4>CONTACT US</h4>
    <div class="row"><svg width="6" height="6" viewBox="0 0 10 10"><path d="M2 0l2 2-1 2c1 1 2 2 3 3l2-1 2 2-2 2C4 10 0 6 0 2z" fill="#5a5a5a"/></svg>+31 (0)20 5550 148</div>
    <div class="row"><svg width="6" height="5" viewBox="0 0 10 8"><rect width="10" height="8" fill="#5a5a5a"/><path d="M0 0l5 4 5-4" fill="none" stroke="#141414"/></svg>info@verantis.example</div>
    <div class="row"><svg width="5" height="6" viewBox="0 0 8 10"><path d="M4 10L1 5a3.5 3.5 0 116 0z" fill="#5a5a5a"/></svg>address Verantis Leiden</div>
  </div>
</footer>
<div class="bottombar">Copyright © 2105 <b>VERANTIS.</b> All Rights Reserved.</div>
</body>
</html>
```